Wendale Ridge Concrete Pumping needs a logo design and is in the concrete industry

A creative design for this Wendale Ridge Concrete Pumping business. Using a trailer mounted line pump, not a boom pump.
Colour to be used is orange and a mix of white or black writing.
Target Market(s)
General Public, anyone
Industry/Entity Type
Concrete
Contact Information for Business Card
Wendale Ridge Concrete Pumping
Callum Hesketh
PO BOX 47
Tarrowen VIC 3268
Phone: 0417952803
Email: Hesketh@bluewrenmail.com.au
Colors
f37122
000000
ffffff
Requirements
Must have
- Details listed
Nice to have
- A great logo
Should not have
- anything silly

```html
<!DOCTYPE html>
<html lang="en">
<head>
<meta charset="utf-8">
<title>Wendale Ridge Concrete Pumping – Business Card</title>
<link rel="stylesheet" href="https://fonts.googleapis.com/css2?family=Arimo:wght@400;700&display=swap">
<style>
  :root {
    --backdrop: #55585a;
    --card: #1c1c1d;
    --emboss: #3a3a3c;
    --orange: #f37122;
    --white: #ffffff;
    --grey: #9a9a9a;
  }
  * { box-sizing: border-box; margin: 0; padding: 0; }
  html, body { width: 802px; height: 1200px; overflow: hidden; }
  body {
    background: var(--backdrop);
    font-family: "Arimo", Arial, sans-serif;
    display: flex;
    flex-direction: column;
    align-items: center;
    justify-content: space-around;
    padding: 70px 0;
  }
  .card {
    width: 640px;
    height: 366px;
    background: var(--card);
    box-shadow: 0 14px 30px rgba(0,0,0,0.45);
    position: relative;
  }

  /* Front */
  .card--front {
    display: flex;
    align-items: center;
    justify-content: center;
  }
  .brand {
    display: flex;
    align-items: center;
    gap: 18px;
  }
  .brand__dot {
    width: 34px;
    height: 34px;
    border-radius: 50%;
    flex: none;
  }
  .brand__name {
    font-weight: 400;
    line-height: 1.15;
  }
  .brand__name span { display: block; }
  .card--front .brand__dot { background: var(--emboss); }
  .card--front .brand__name { color: var(--emboss); font-size: 40px; }
  .card--front .brand__name .brand__sub { font-size: 20px; letter-spacing: 6px; text-transform: uppercase; margin-top: 6px; }

  /* Back */
  .card--back {
    display: flex;
    align-items: center;
    padding: 0 30px 0 40px;
  }
  .card--back .brand { width: 268px; gap: 12px; flex: none; }
  .card--back .brand__dot { background: var(--orange); width: 26px; height: 26px; }
  .card--back .brand__name { color: var(--grey); font-size: 25px; }
  .card--back .brand__name .brand__sub { font-size: 12.5px; letter-spacing: 3px; text-transform: uppercase; margin-top: 5px; }
  .divider {
    width: 2px;
    height: 150px;
    background: var(--orange);
    margin: 0 24px 0 12px;
    flex: none;
  }
  .contact { color: var(--white); font-size: 17px; line-height: 1.55; }
  .contact__name {
    color: var(--orange);
    font-weight: 700;
    text-transform: uppercase;
    font-size: 17px;
    margin-bottom: 8px;
  }
  .contact__row { display: flex; align-items: center; gap: 8px; white-space: nowrap; }
  .contact__icon { width: 14px; height: 14px; flex: none; fill: var(--orange); }
</style>
</head>
<body>
  <section class="card card--front" aria-label="Business card front">
    <div class="brand">
      <span class="brand__dot"></span>
      <p class="brand__name"><span>Wendale Ridge</span><span class="brand__sub">Concrete Pumping</span></p>
    </div>
  </section>

  <section class="card card--back" aria-label="Business card back">
    <div class="brand">
      <span class="brand__dot"></span>
      <p class="brand__name"><span>Wendale Ridge</span><span class="brand__sub">Concrete Pumping</span></p>
    </div>
    <div class="divider"></div>
    <div class="contact">
      <p class="contact__name">Callum Hesketh</p>
      <p class="contact__row">PO BOX 47 Tarrowen VIC 3268</p>
      <p class="contact__row">
        <svg class="contact__icon" viewBox="0 0 14 14" aria-hidden="true"><path d="M3 1h3l1 3-2 1.5a7 7 0 0 0 3.5 3.5L10 7l3 1v3a2 2 0 0 1-2 2A10 10 0 0 1 1 3a2 2 0 0 1 2-2z"/></svg>
        0417952803
      </p>
      <p class="contact__row">
        <svg class="contact__icon" viewBox="0 0 14 14" aria-hidden="true"><path d="M0 3h14v8H0z M0 3l7 5 7-5" fill="var(--orange)" stroke="var(--card)" stroke-width="1"/></svg>
        Hesketh@bluewrenmail.com.au
      </p>
    </div>
  </section>
</body>
</html>
```